Capability statement for an Electrical Business based in Sydney Australia

The aim for the Capability statement is for us to look more professional when we meet someone or after cold calling and have to send them our business details.
Need something simple, efficient and to the point.

It should have the following content
- Our mission (details can be as attached PDF)
- Areas we service (this can be a google map of areas we service but basically the areas are
Metro Sydney with our work centralised around the Norwest, Hills, Inner west and Epping area)
- List of services we provide (as PDF)
- Details about us; who we are, contact details, licenses (as PDF)
- Why they should choose us
(As pdf)

Right now, we're just after a nice format we're happy with, the details we are happy to provide with once we have a design in mind.

I've attached our current existing capability statement and what our details are. Also, our website is
https://themardenfield.com.au/

Thanks in advance!

• Should not be complicated for the reader

```html
<!DOCTYPE html>
<html lang="en">
<head>
<meta charset="utf-8">
<title>The Marden Field – Capability Statement</title>
<link href="https://fonts.googleapis.com/css2?family=Poppins:wght@400;500;600;700;800&display=swap" rel="stylesheet">
<style>
  :root{
    --red:#e8262b;
    --black:#0d0d0d;
    --ink:#1b1b1b;
    --paper:#ffffff;
    --stone:#ececec;
    --stage:#3a3a3c;
  }
  *{box-sizing:border-box;margin:0;padding:0}
  html,body{width:1200px;height:776px;overflow:hidden}
  body{background:var(--stage);font-family:"Poppins",sans-serif;color:var(--ink);position:relative}
  .page{position:absolute;top:18px;width:523px;height:740px;background:var(--paper);overflow:hidden;box-shadow:0 10px 30px rgba(0,0,0,.45)}
  .page--front{left:40px}
  .page--back{left:637px}
  .header-art{position:absolute;left:0;top:0;width:523px;height:126px}
  .brand{position:absolute;display:flex;align-items:center;gap:7px;font-weight:700;font-size:18px;letter-spacing:.3px;font-family:"Poppins",sans-serif;white-space:nowrap}
  .brand__dot{width:11px;height:11px;border-radius:50%;background:var(--red)}
  .page--front .brand{left:24px;top:46px;color:var(--black)}
  .page--back .brand{left:24px;top:46px;color:var(--paper)}

  /* front */
  .front-body{position:absolute;left:0;top:126px;width:523px;height:514px;background:linear-gradient(135deg,#f1f1f1,#e2e2e2 60%,#efefef)}
  .why-panel{position:absolute;left:0;top:40px;width:285px;height:455px;background:var(--black);border-radius:0 46px 0 46px;overflow:hidden;color:var(--paper);padding:22px 16px 0 14px}
  .why-photo{position:absolute;right:0;bottom:0;width:170px;height:230px;background:radial-gradient(ellipse at 60% 55%,#4f6a2a 0%,#22301a 40%,rgba(13,13,13,0) 75%)}
  .why-panel__title{position:relative;font-size:8px;font-weight:700;letter-spacing:.3px;padding-bottom:4px;border-bottom:1px solid #fff;width:190px;margin-bottom:22px}
  .reason{position:relative;margin-bottom:17px}
  .reason__title{font-size:8.6px;font-weight:500;margin-bottom:3px}
  .reason__text{font-size:5.6px;line-height:1.35;color:#dcdcdc;max-width:220px}
  .services{position:absolute;left:300px;top:58px;width:210px}
  .services__kicker{font-size:9px;font-weight:700;color:var(--black);line-height:1.1}
  .services__title{font-size:15px;font-weight:800;color:var(--red);line-height:1.1;margin-bottom:16px}
  .services__list{list-style:none}
  .services__list li{position:relative;padding-left:13px;font-size:8.3px;line-height:1.25;margin-bottom:10px;color:var(--black)}
  .services__list li::before{content:"";position:absolute;left:0;top:3px;width:5px;height:5px;border-radius:50%;background:var(--red)}
  .contact-label{font-size:12px;font-weight:700;color:var(--red)}
  .contact-line{font-size:9px;line-height:1.35;display:flex;align-items:center;gap:6px}
  .contact-line::before{content:"";border-left:6px solid var(--red);border-top:4px solid transparent;border-bottom:4px solid transparent}
  .front-footer .phones{position:absolute;left:18px;top:665px}
  .front-footer .licence{position:absolute;left:300px;top:640px}

  /* back */
  .who-banner{position:absolute;left:18px;top:150px;width:300px;height:40px;background:linear-gradient(90deg,var(--red) 55%,rgba(232,38,43,0));color:var(--paper);font-weight:800;font-size:21px;padding:4px 0 0 18px}
  .who-text{position:absolute;left:36px;top:208px;width:455px;font-size:10.6px;line-height:1.4;color:var(--black)}
  .who-text p{margin-bottom:12px}
  .mission{position:absolute;left:18px;top:368px;width:505px;height:175px;background:linear-gradient(180deg,#2a2a2a 0%,#3a3530 60%,#8a7a64 100%);color:var(--paper);padding:22px 30px}
  .mission__title{font-size:27px;font-weight:800;color:var(--red);line-height:1}
  .mission__text{font-size:12px;line-height:1.35;margin-top:10px;max-width:430px}
  .back-footer{position:absolute;left:18px;top:543px;width:505px;height:197px;background:var(--paper);padding:18px 22px}
  .back-footer .col{position:absolute}
  .back-footer .col--left{left:22px;top:20px}
  .back-footer .col--right{left:300px;top:14px}
  .back-footer .contact-label{font-size:11.5px;margin-top:8px}
  .back-footer .contact-line{font-size:8.5px}
  .entity{color:var(--red);font-size:8px}
</style>
</head>
<body>

<section class="page page--front" aria-label="Capability statement front">
  <svg class="header-art" viewBox="0 0 523 126">
    <defs>
      <linearGradient id="kitchenTone" x1="0" y1="0" x2="1" y2="1">
        <stop offset="0" stop-color="#f2efe9"/><stop offset=".6" stop-color="#d8d4cc"/><stop offset="1" stop-color="#9a958e"/>
      </linearGradient>
    </defs>
    <polygon points="235,0 523,0 523,112 300,112" fill="url(#kitchenTone)" role="img" aria-label="Photo of a bright modern kitchen"/>
    <polygon points="215,0 237,0 302,112 280,112" fill="#0d0d0d"/>
    <rect x="0" y="112" width="523" height="14" fill="#0d0d0d"/>
  </svg>
  <div class="brand"><span class="brand__dot"></span>The Marden Field</div>

  <div class="front-body">
    <div class="why-panel">
      <div class="why-photo" role="img" aria-label="Photo of a garden lamp lit among plants at night"></div>
      <div class="why-panel__title">WHY CHOOSE THE MARDEN FIELD</div>
      <div class="reason">
        <div class="reason__title">Support when you need it most :</div>
        <div class="reason__text">We provide around the clock assistance, whether during normal business hours or emergencies we are focused on providing solutions for our clients.</div>
      </div>
      <div class="reason">
        <div class="reason__title">Fast and responsive team with a direct contact :</div>
        <div class="reason__text">We treat every one of our clients as a VIP. We pride ourselves on being able to provide a quick turn around for all our jobs. We make the whole process smooth, from booking the job to attending and completion.</div>
      </div>
      <div class="reason">
        <div class="reason__title">Satisfaction with loyalty and integrity :</div>
        <div class="reason__text">We value our transparency and communication skills to deliver an outstanding performance which reflects our happy customer base.</div>
      </div>
      <div class="reason">
        <div class="reason__title">We provide courtesy calls :</div>
        <div class="reason__text">The appointment will be confirmed the day before and our technicians will call you half an hour in advance on approach to the job.</div>
      </div>
      <div class="reason">
        <div class="reason__title">Licensed and insured technicians :</div>
        <div class="reason__text">All our technicians are experts of their field, with the relevant equipment, knowledge and licenses to carry out our duties.</div>
      </div>
    </div>

    <div class="services">
      <div class="services__kicker">Brief List of the most common</div>
      <div class="services__title">services we provide</div>
      <ul class="services__list">
        <li>24/7 Emergency service</li>
        <li>Switchboard UPGRADE and REPAIRS</li>
        <li>Powerpoint installations</li>
        <li>Surge device installations</li>
        <li>Testing and servicing electric hot water systems</li>
        <li>Smoke Alarm installation with compliance certificate</li>
        <li>Electric Vehicle charging stations</li>
        <li>Ceiling and Exhaust fan installations with roof and wall venting</li>
        <li>Appliance installations</li>
        <li>Fault finding</li>
        <li>TV, DATA and FREE TO AIR Aerial installations</li>
      </ul>
    </div>
  </div>

  <div class="front-footer">
    <div class="phones">
      <div class="contact-label">Mobile Phone Number</div>
      <div class="contact-line">0412 555 018</div>
      <div class="contact-line">0455501234</div>
    </div>
    <div class="licence">
      <div class="contact-label">Electrical license number</div>
      <div class="contact-line">318802C</div>
      <div class="contact-line">402715C</div>
    </div>
  </div>
</section>

<section class="page page--back" aria-label="Capability statement back">
  <svg class="header-art" viewBox="0 0 523 126">
    <defs>
      <linearGradient id="roomTone" x1="0" y1="0" x2="1" y2="1">
        <stop offset="0" stop-color="#f4f2ee"/><stop offset=".7" stop-color="#dedbd4"/><stop offset="1" stop-color="#c2bdb3"/>
      </linearGradient>
    </defs>
    <rect x="0" y="0" width="523" height="126" fill="#0d0d0d"/>
    <polygon points="215,0 523,0 523,112 290,112" fill="url(#roomTone)" role="img" aria-label="Photo of a bright kitchen with windows and plants"/>
    <rect x="0" y="112" width="523" height="14" fill="#0d0d0d"/>
    <rect x="0" y="126" width="523" height="614" fill="#f3f3f3"/>
  </svg>
  <div class="brand"><span class="brand__dot"></span>The Marden Field</div>

  <div class="who-banner">WHO WE ARE</div>
  <div class="who-text">
    <p>The Marden Field is a growing Electrical maintenance company based in the Inner West.</p>
    <p>We are established on sound service principles with honesty, communication, and respect at the forefront of every team member.</p>
    <p>We strive for openness, trust, and accountability and we are in the business of providing solutions to help others. We see ourselves as an extension of your team.</p>
  </div>

  <div class="mission" role="img" aria-label="Photo of a warmly lit living room behind the mission statement">
    <div class="mission__title">MISSION</div>
    <div class="mission__text">Dedicate ourselves to providing world class service to anyone in need, based on honesty, communication and respect</div>
  </div>

  <div class="back-footer">
    <div class="col col--left">
      <div class="contact-label">Mobile Phone Number</div>
      <div class="contact-line">0412 555 018</div>
      <div class="contact-line">0455501234</div>
      <div class="contact-label">Electrical license number</div>
      <div class="contact-line">318802C <span class="entity">The Marden Field Pty Ltd</span> (461207C)</div>
      <div class="contact-line">402715C</div>
    </div>
    <div class="col col--right">
      <div class="contact-label">Email</div>
      <div class="contact-line">services@themardenfield.com.au</div>
      <div class="contact-label">ABN</div>
      <div class="contact-line">5182 4407 316</div>
      <div class="contact-label">Public Liability</div>
      <div class="contact-line">$20,000,000</div>
    </div>
  </div>
</section>

</body>
</html>
```